Kestrel Learning Consultancy needs a colourful yet professional website

I am looking for a clean, colourful yet professional website that will appeal to schools and families looking for training and consultancy for children with and without special needs. The company is called Kestrel Learning Consultancy. I would be open to stock images being used and I attach my logo in the files below which should complement the design of the website. My strap line is 'achieve believe succeed' A website which offers similar services that I like the menu layout of is www.tovamplex.com. I would initially be looking at 7 main title links of: Home, About, Services, Team/Careers, Events, Links, Contact Us. The services title should have a drop down menu linking to Parents, Schools, Training, Professional Development, Supervision. Each page would contain fixed text with stock images where appropriate, bar the Events page where it may be laid out differently to display separate course events coming up. A contact us form would be required under the relevant tab. Ideas of formats, templates, logo etc are attached below. I look forward to reviewing designs!

Target Market(s)

Families and Schools

Industry/Entity Type

Education

Coding

Coded - Design and coding required

Font styles to use
Sans Serif

Requirements
Must have
• Logo incorporated
• Easy to read font
• Easy to navigate
Should not have
• Ultra modern minimalist style
• Dark colours

```html
<!DOCTYPE html>
<html lang="en">
<head>
<meta charset="utf-8">
<title>Kestrel Learning Consultancy</title>
<link href="https://fonts.googleapis.com/css2?family=Roboto:wght@400;500&family=Open+Sans:wght@400;600&display=swap" rel="stylesheet">
<style>
:root{
  --red:#c1121c;
  --red-dark:#a50d16;
  --green:#8dc63f;
  --lime:#a7c13c;
  --pink:#d3878f;
  --brown:#5c4420;
  --brown-text:#5a4526;
  --sky:#8ecbf6;
  --sky-light:#dff0fc;
  --salmon:#e16a69;
  --grey:#777;
  --white:#fff;
}
*{box-sizing:border-box;margin:0;padding:0}
html,body{width:686px;height:1200px;overflow:hidden;background:var(--white)}
body{position:relative;font-family:"Open Sans",Arial,sans-serif;color:var(--grey)}
.abs{position:absolute}

/* header + hero */
.hero{left:0;top:0;width:686px;height:382px;background:linear-gradient(180deg,#a9d6f7 0%,#e6f3fc 45%,#f3f9fd 62%,#b6dc6a 78%,#7fbf2e 100%)}
.brand{left:0;top:22px;width:686px;text-align:center;font-family:"Roboto",sans-serif}
.brand-mark{display:inline-block;width:12px;height:12px;border-radius:50%;background:var(--green);margin-right:6px;vertical-align:middle}
.brand-name{font-size:22px;font-weight:500;color:var(--brown-text);vertical-align:middle}
.brand-tag{font-size:6px;color:var(--red);margin-top:1px}
.nav{left:73px;top:86px;width:540px;height:30px;background:linear-gradient(180deg,#d01820,var(--red-dark));display:flex}
.nav a{color:var(--white);text-decoration:none;font-size:8.5px;font-family:"Open Sans",sans-serif;font-weight:600;display:flex;align-items:center;justify-content:center;border-right:1px solid rgba(255,255,255,.25);height:100%}
.nav a:last-child{border-right:0}
.hero-title{left:76px;top:180px;font-family:"Roboto",sans-serif;font-size:20px;line-height:26px}
.hero-title .lead{color:var(--green)}
.hero-title .main{color:var(--red)}
.hero-copy{left:77px;top:238px;width:240px;font-size:7px;line-height:12px;color:#555}
.btn{display:flex;align-items:center;justify-content:center;color:var(--white);font-size:7px;border-radius:3px}
.hero-btn{left:77px;top:270px;width:68px;height:20px;background:var(--salmon);text-transform:uppercase}
.dots{left:80px;top:302px;display:flex;gap:3px}
.dots span{width:9px;height:9px;border-radius:50%;background:var(--white)}
.dots span:first-child{background:transparent;border:1px solid var(--white)}
.hero-photo{left:316px;top:132px;width:300px;height:250px;background:radial-gradient(ellipse at 50% 45%,#e9b89a 0%,#d59a7c 35%,rgba(120,170,80,.3) 75%,rgba(0,0,0,0) 100%);border-radius:40% 40% 0 0}

/* about */
.about-title{left:0;top:410px;width:686px;text-align:center;font-family:"Roboto",sans-serif;font-size:16px;color:var(--red)}
.about-copy{left:100px;top:438px;width:486px;text-align:center;font-size:7.5px;line-height:13px;color:#888}
.service{top:494px;width:116px;height:116px;border-radius:50%;display:flex;flex-direction:column;align-items:center;justify-content:center;color:var(--white);font-family:"Roboto",sans-serif;font-size:9.5px;line-height:11px;text-align:center}
.service::after{content:"";position:absolute;inset:4px;border-radius:50%;border:1px dashed rgba(255,255,255,.35)}
.service svg{width:30px;height:30px;margin-bottom:3px}
.s1{left:92px;background:#9dbb3a}
.s2{left:223px;background:var(--pink)}
.s3{left:354px;background:var(--brown)}
.s4{left:484px;background:var(--sky)}

/* team */
.team{left:0;top:634px;width:686px;height:250px;background:linear-gradient(90deg,#b8cde0 0%,#e9e4da 30%,#e0b59a 55%,#d39b7d 70%,#4f86c7 100%)}
.team-curve{left:0;top:850px;width:686px;height:40px}
.team-panel{left:80px;top:634px;width:210px;height:232px;background:rgba(255,255,255,.82)}
.team-title{left:80px;top:676px;width:210px;text-align:center;font-family:"Roboto",sans-serif;font-size:15px;color:var(--brown-text)}
.team-sub{left:100px;top:704px;width:170px;text-align:center;font-size:7px;line-height:12px;color:#444}
.team-copy{left:102px;top:736px;width:166px;text-align:center;font-size:6.2px;line-height:11.5px;color:#888}
.team-btn{left:146px;top:794px;width:68px;height:22px;background:var(--lime);border-radius:11px;font-size:8px}

/* events */
.events-title{left:0;top:906px;width:686px;text-align:center;font-family:"Roboto",sans-serif;font-size:17px;color:var(--brown-text)}
.card{top:942px;width:161px;height:156px;border:1px solid #e2e2e2;background:var(--white)}
.card-photo{height:82px}
.card-body{padding:12px 14px 0}
.card-title{font-family:"Roboto",sans-serif;font-size:9.5px;color:var(--red)}
.card-copy{font-size:6.3px;line-height:12px;color:#777;margin-top:3px}
.card-date{font-size:6.3px;color:#7aa21f;font-weight:600;margin-top:2px}
.c1{left:86px}.c2{left:262px}.c3{left:436px}
.p1{background:linear-gradient(135deg,#c84a3c,#e7c9b5 50%,#3c3a44)}
.p2{background:linear-gradient(180deg,#a7c28a,#dcd2c2 55%,#6c8c4a)}
.p3{background:linear-gradient(135deg,#7fb6e6,#f0c9a8 45%,#e9b7a0 70%,#5f93d1)}

/* footer */
.footer{left:0;top:1126px;width:686px;height:74px;background:var(--lime)}
.footer-nav{left:81px;top:1146px;display:flex;gap:0;font-size:7.5px;color:var(--white)}
.footer-nav span{margin-right:22px}
.footer-legal{left:81px;top:1161px;font-size:6px;color:var(--white)}
.social{left:530px;top:1143px;display:flex;gap:4px}
.social span{width:16px;height:16px;border-radius:50%;border:1px solid var(--white)}
</style>
</head>
<body>

<div class="abs hero"></div>
<div class="abs hero-photo" role="img" aria-label="Photo of four smiling children standing together"></div>

<div class="abs brand">
  <span class="brand-mark"></span><span class="brand-name">Kestrel</span>
  <div class="brand-tag">Learning Consultancy</div>
</div>

<nav class="abs nav">
  <a style="width:76px">HOME</a>
  <a style="width:64px">ABOUT</a>
  <a style="width:76px">SERVICES</a>
  <a style="width:104px">TEAM/CAREERS</a>
  <a style="width:66px">EVENTS</a>
  <a style="width:52px">LINKS</a>
  <a style="width:102px">CONTACT US</a>
</nav>

<div class="abs hero-title">
  <div class="lead">Welcome to Kestrel</div>
  <div class="main">Learning Consultancy</div>
</div>
<p class="abs hero-copy">Cum sociis natoque penatibus et magnis dis parturient montes nascetur ridiculus mus In iaculis facilisis massa</p>
<div class="abs btn hero-btn">Read More</div>
<div class="abs dots"><span></span><span></span><span></span><span></span></div>

<h2 class="abs about-title">About Kestrel Learning Consultancy</h2>
<p class="abs about-copy">venenatis nec euismod sit amet egestas placerat est Pellentesque habitant morbi tristique senectus et netus et malesuada fames ac turpis egestas Cras id elit Integer quis urna Ut ante enim dapibus malesuada</p>

<div class="abs service s1">
  <svg viewBox="0 0 30 30" fill="none" stroke="#fff" stroke-width="1.4"><circle cx="10" cy="5" r="3"/><path d="M6 28V12h8v16M10 18v10"/><circle cx="21" cy="13" r="2.4"/><path d="M18 28v-10h6v10"/></svg>
  Parent<br>Sibling Training
</div>
<div class="abs service s2">
  <svg viewBox="0 0 30 30" fill="none" stroke="#fff" stroke-width="1.4"><path d="M8 28V9l4-5 4 5v19M8 14h8M8 20h8M16 16l10 12"/></svg>
  Group<br>Services
</div>
<div class="abs service s3">
  <svg viewBox="0 0 30 30" fill="none" stroke="#fff" stroke-width="1.4"><path d="M3 15l12-10 12 10M6 13v14h18V13M12 27v-7h6v7"/></svg>
  In home Early<br>Intervention
</div>
<div class="abs service s4">
  <svg viewBox="0 0 30 30" fill="none" stroke="#fff" stroke-width="1.4"><rect x="3" y="3" width="11" height="7" rx="2"/><circle cx="19" cy="14" r="4"/><path d="M11 28c0-6 4-9 8-9s8 3 8 9z"/></svg>
  Parents<br>Consultancy
</div>

<div class="abs team" role="img" aria-label="Photo of two smiling girls drawing with coloured pencils"></div>
<div class="abs team-panel"></div>
<svg class="abs team-curve" viewBox="0 0 686 40" preserveAspectRatio="none"><path d="M0 26 Q343 2 686 26 V40 H0Z" fill="#fff"/></svg>
<h3 class="abs team-title">Team/Career</h3>
<p class="abs team-sub">Avenenatis nec euismod sit amet egestas placerat est Pellentesque habitant</p>
<p class="abs team-copy">Tristique senectus et netus et malesuada fames ac turpis egestas Cras id elit Integer quis urna Ut ante enim dapibus malesuada fringilla eu condimentum quis tellus Aenean porttitor eros</p>
<div class="abs btn team-btn">Read More</div>

<h2 class="abs events-title">Latest Events</h2>

<article class="abs card c1">
  <div class="card-photo p1" role="img" aria-label="Photo of children in pirate costumes at a party"></div>
  <div class="card-body">
    <div class="card-title">Cras a ante vitae enim</div>
    <p class="card-copy">iaculis aliquam Mauris nunc quam venenatis nec euismod sit amet egesta</p>
    <div class="card-date">05 April 2016</div>
  </div>
</article>
<article class="abs card c2">
  <div class="card-photo p2" role="img" aria-label="Photo of children running and playing outdoors"></div>
  <div class="card-body">
    <div class="card-title">Cras a ante vitae enim</div>
    <p class="card-copy">iaculis aliquam Mauris nunc quam venenatis nec euismod sit amet egesta</p>
    <div class="card-date">05 April 2016</div>
  </div>
</article>
<article class="abs card c3">
  <div class="card-photo p3" role="img" aria-label="Photo of a group of smiling children lying together"></div>
  <div class="card-body">
    <div class="card-title">Cras a ante vitae enim</div>
    <p class="card-copy">iaculis aliquam Mauris nunc quam venenatis nec euismod sit amet egesta</p>
    <div class="card-date">05 April 2016</div>
  </div>
</article>

<footer class="abs footer"></footer>
<div class="abs footer-nav"><span>HOME</span><span>ABOUT</span><span>SERVICES</span><span>TEAM/CAREERS</span><span>EVENTS</span><span>LINKS</span><span>CONTACT US</span></div>
<div class="abs footer-legal">© 2016 Company Name. All right reserved. Term of Use</div>
<div class="abs social"><span></span><span></span><span></span><span></span></div>

</body>
</html>
```